K.L.T Services

We are needing business cards for a construction company that does everything from painting and detailing, maintenance, Sheetrock repairs, demolition, tile and wood floors. Also, K.L.T stands for Detailing, maintenance, and Painting. We would like the colors to be closer to the colors grey and light brown/khaki, but if there is any other suggestions that would go better with the design we are open to ideas.

Industry/Entity Type

Business

Contact Information for Business Card

Owner / Operator Owen Salcedo (555) 318-4927 / (555) 742- 0386

Font styles to use
Sans Serif

```html
<!DOCTYPE html>
<html lang="en">
<head>
<meta charset="utf-8">
<title>K.L.T Services – Business Card</title>
<link rel="stylesheet" href="https://fonts.googleapis.com/css2?family=Source+Sans+3:wght@300;400;600;700&display=swap">
<style>
  :root {
    --backdrop: #ecebe8;
    --card-white: #ffffff;
    --khaki: #bcae98;
    --khaki-text: #b3a38a;
    --band-grey: #d9d9db;
    --soft-grey: #c9c9cc;
    --rule-grey: #cfcfd1;
    --on-khaki: #ffffff;
  }
  * { box-sizing: border-box; margin: 0; padding: 0; }
  html, body {
    width: 1200px;
    height: 902px;
    overflow: hidden;
    background: var(--backdrop);
    font-family: "Source Sans 3", "Myriad Pro", sans-serif;
  }
  .business-card {
    position: absolute;
    left: 100px;
    top: 165px;
    width: 1000px;
    height: 572px;
    background: var(--card-white);
    box-shadow: 0 10px 30px rgba(0,0,0,0.12);
    overflow: hidden;
  }
  .brand {
    position: absolute;
    top: 60px;
    left: 0;
    width: 100%;
    text-align: center;
  }
  .brand-name {
    display: inline-flex;
    align-items: center;
    gap: 14px;
    font-size: 76px;
    font-weight: 700;
    line-height: 1;
    color: var(--khaki-text);
    letter-spacing: 2px;
  }
  .brand-dot {
    width: 22px;
    height: 22px;
    border-radius: 50%;
    background: var(--khaki-text);
  }
  .tagline-main {
    margin-top: 22px;
    font-size: 40px;
    font-weight: 700;
    color: var(--khaki-text);
    line-height: 1;
  }
  .tagline-sub {
    margin: 10px auto 0;
    width: 640px;
    display: flex;
    align-items: center;
    gap: 20px;
    font-size: 38px;
    font-weight: 300;
    color: var(--soft-grey);
    line-height: 1;
  }
  .tagline-sub .rule {
    flex: 1;
    height: 2px;
    background: var(--rule-grey);
  }
  .divider-band {
    position: absolute;
    left: 0;
    top: 330px;
    width: 100%;
    height: 20px;
    background: var(--band-grey);
  }
  .info-panel {
    position: absolute;
    left: 0;
    top: 350px;
    width: 100%;
    height: 222px;
    background: var(--khaki);
    color: var(--on-khaki);
  }
  .holder {
    position: absolute;
    left: 60px;
    bottom: 44px;
  }
  .holder-name {
    font-size: 40px;
    font-weight: 700;
    line-height: 1.1;
  }
  .holder-role {
    font-size: 34px;
    font-weight: 400;
    line-height: 1.15;
  }
  .contact {
    position: absolute;
    right: 60px;
    top: 36px;
    font-size: 26px;
    font-weight: 400;
    line-height: 1.3;
  }
  .contact-row {
    display: flex;
    align-items: flex-start;
    gap: 12px;
  }
  .contact-row + .contact-row { margin-top: 10px; }
  .contact-icon {
    width: 22px;
    height: 22px;
    margin-top: 6px;
    flex: none;
  }
  .contact-icon.at {
    font-weight: 700;
    font-size: 26px;
    margin-top: 0;
    text-align: center;
  }
</style>
</head>
<body>
  <div class="business-card">
    <div class="brand">
      <div class="brand-name"><span class="brand-dot"></span>K.L.T</div>
      <div class="tagline-main">Kitchens, landscaping &amp;</div>
      <div class="tagline-sub"><span class="rule"></span>tiling<span class="rule"></span></div>
    </div>

    <div class="divider-band"></div>

    <div class="info-panel">
      <div class="contact">
        <div class="contact-row">
          <svg class="contact-icon" viewBox="0 0 24 24" aria-hidden="true">
            <path fill="#ffffff" d="M6.6 10.8a15.1 15.1 0 0 0 6.6 6.6l2.2-2.2a1 1 0 0 1 1-.25 11.4 11.4 0 0 0 3.6.57 1 1 0 0 1 1 1V20a1 1 0 0 1-1 1A17 17 0 0 1 3 4a1 1 0 0 1 1-1h3.5a1 1 0 0 1 1 1c0 1.25.2 2.45.57 3.570a1 1 0 0 1-.25 1z"/>
          </svg>
          <div>(555) 318-4927<br>(555) 742- 0386</div>
        </div>
        <div class="contact-row">
          <span class="contact-icon at">@</span>
          <div>info@kltservices.com</div>
        </div>
      </div>

      <div class="holder">
        <div class="holder-name">Owen Salcedo</div>
        <div class="holder-role">Owner / Operator</div>
      </div>
    </div>
  </div>
</body>
</html>
```